Cake website needs a professional WordPress design makeover!

I need a wordpress design for my company called Velvet Crumbhouse. It's a home cake business and I specialise in everything from cupcakes, celebratory cakes to couture wedding cakes. I have an existing one page wordpress website www.velvetcrumbhouse.example but it doesn't quite communicate elegance or showcase my skills so it desperately needs a complete change.

I purchased this theme
http://lumatheme.example/demos/themes/?product=vela
I basically want my website to look EXACTLY like this. I would obviously provide pictures of my work. I like the positioning of the pictures and texts and how each section are divided with the pictures. I also like the pop up of the welcome text on the home page. I would like that to say Welcome Velvet Crumbhouse.

One element I would like to keep from my original website are the slides on the home page. But will have a different caption with each slide. I will provide the three pictures for these slides.

The page format should be as follows:

Home
Discover Our Story
Tasteful Delights (Picture)
Discover Our Cakes - Clickable link below description going to the full cake menu with prices
The Perfect Blend (Picture)
Our Promise
Discover Your Special Day (Picture)
Wedding Cakes
Make an Order (Picture)
Get in touch

The menu on top of the page should read
Home, Our story, Our Cakes, Price List, Wedding cakes, Get in Touch

I would like to see the page of the full cake menu with the prices.
Signature colours Black, White and Pink

Target Market(s)

My main audience is targeted at women.

Industry/Entity Type

Wedding

Requirements
Must have
• Must look like the link I provided. Please use this as reference.
Nice to have
• Nice to see aspects of my logo, example the butterflies or the paisley design be subtly used around the website.

```html
<!DOCTYPE html>
<html lang="en">
<head>
<meta charset="utf-8">
<title>Velvet Crumbhouse</title>
<link rel="stylesheet" href="https://fonts.googleapis.com/css2?family=Pinyon+Script&family=Cinzel:wght@400;500&family=Open+Sans:wght@400;600&family=Nunito:wght@400;600&display=swap">
<style>
  :root {
    --pink: #d9837f;
    --pink-dark: #c66f6c;
    --pink-soft: #dfa3a4;
    --pink-label: #d9807c;
    --ink: #1d1d1d;
    --body-text: #555555;
    --white: #ffffff;
    --black: #000000;
    --footer: #2f2f2f;
    --footer-text: #8a8a8a;
    --field-text: #8f8f8f;
    --divider: #dddddd;
  }
  * { box-sizing: border-box; margin: 0; padding: 0; }
  html, body { width: 1200px; height: 2715px; overflow: hidden; }
  body { position: relative; background: var(--white); font-family: "Open Sans", Arial, sans-serif; color: var(--body-text); }
  .abs { position: absolute; }

  /* Navigation */
  .nav-bar {
    left: 124px; top: 104px; width: 958px; height: 62px;
    background: linear-gradient(180deg, var(--pink) 0%, var(--pink-dark) 100%);
  }
  .nav-bar::after {
    content: ""; position: absolute; left: 0; right: 0; bottom: -6px; height: 6px;
    background: radial-gradient(circle at 50% 0, var(--pink-dark) 5px, transparent 5.6px) repeat-x;
    background-size: 11px 6px;
  }
  .nav-link {
    position: absolute; top: 23px; font-family: "Nunito", Arial, sans-serif;
    font-size: 15px; font-weight: 600; color: var(--white); text-decoration: none;
  }
  .logo-card {
    left: 478px; top: 27px; width: 249px; height: 218px; background: var(--white);
    border-radius: 6px; box-shadow: 0 3px 10px rgba(0,0,0,.25);
    display: flex; align-items: center; justify-content: center; gap: 10px; z-index: 3;
  }
  .logo-mark { width: 16px; height: 16px; border-radius: 50%; background: var(--pink-soft); }
  .logo-name { font-family: "Pinyon Script", cursive; font-size: 34px; color: var(--pink-dark); }

  /* Hero slider */
  .hero {
    left: 124px; top: 169px; width: 958px; height: 458px; overflow: hidden;
    background: linear-gradient(120deg, #e7a2aa 0%, #5a3325 30%, #e9c9c4 50%, #4a2a20 70%, #ec9aa4 100%);
  }
  .slider-arrow {
    position: absolute; top: 183px; width: 40px; height: 64px; background: rgba(255,255,255,.55);
  }
  .slider-arrow.prev { left: 0; border-radius: 0 32px 32px 0; }
  .slider-arrow.next { right: 0; border-radius: 32px 0 0 32px; }
  .slider-arrow svg { position: absolute; top: 20px; }
  .slider-arrow.prev svg { left: 9px; }
  .slider-arrow.next svg { right: 9px; }
  .scroll-notch { position: absolute; left: 429px; bottom: 0; width: 100px; height: 44px; }

  /* Section type */
  .script-title { font-family: "Pinyon Script", cursive; color: var(--pink-soft); font-size: 88px; line-height: 1; }
  .section-title { font-family: "Cinzel", serif; color: var(--ink); font-size: 34px; letter-spacing: 3px; line-height: 1; }
  .body-copy { font-size: 12.5px; line-height: 22px; color: var(--body-text); }
  .body-copy p + p { margin-top: 6px; }

  .photo { position: absolute; border-radius: 4px; }

  /* Banners */
  .banner { left: 124px; width: 958px; height: 240px; display: flex; flex-direction: column; align-items: center; justify-content: center; }
  .banner::after {
    content: ""; position: absolute; left: 0; right: 0; bottom: -7px; height: 7px;
    background: radial-gradient(circle at 50% 0, #6d6d6d 5px, transparent 5.6px) repeat-x;
    background-size: 11px 7px;
  }
  .banner .script-title { font-size: 78px; color: #e4a2a8; }
  .banner-caption { font-family: "Cinzel", serif; color: var(--white); font-size: 27px; letter-spacing: 3px; margin-top: -14px; }

  /* Price list */
  .price-item { position: absolute; font-family: "Nunito", Arial, sans-serif; }
  .price-name { font-size: 12.5px; color: var(--pink-label); }
  .price-value { font-size: 15px; color: var(--ink); margin-top: 6px; }
  .price-divider { left: 145px; top: 2123px; width: 402px; height: 1px; background: var(--divider); }

  /* Contact */
  .contact { left: 122px; top: 2249px; width: 958px; height: 342px; background: var(--black); }
  .contact::before {
    content: ""; position: absolute; left: 0; right: 0; top: -7px; height: 7px;
    background: radial-gradient(circle at 50% 100%, var(--black) 5px, transparent 5.6px) repeat-x;
    background-size: 11px 7px;
  }
  .contact .script-title { position: absolute; left: 60px; top: 62px; font-size: 82px; color: var(--pink-soft); }
  .contact .section-title { position: absolute; left: 62px; top: 147px; color: var(--white); font-size: 32px; }
  .field {
    position: absolute; background: var(--white); border-radius: 2px;
    font-size: 11px; color: var(--field-text); padding: 7px 12px;
  }
  .submit-button {
    position: absolute; left: 447px; top: 220px; width: 109px; height: 33px;
    background: var(--pink); color: var(--white); font-family: "Cinzel", serif; font-weight: 500;
    font-size: 14px; letter-spacing: 1.5px; display: flex; align-items: center; justify-content: center;
  }
  .footer { left: 122px; top: 2591px; width: 958px; height: 76px; background: var(--footer); }
  .footer-hump { position: absolute; left: 405px; top: -40px; }
  .footer-note { position: absolute; left: 42px; top: 29px; font-size: 11px; color: var(--footer-text); }
  .social-dot { position: absolute; top: 16px; width: 33px; height: 33px; border-radius: 50%; background: var(--white); }
</style>
</head>
<body>

  <!-- Header -->
  <nav class="abs nav-bar">
    <a class="nav-link" style="left:31px">Home</a>
    <a class="nav-link" style="left:100px">Our Story</a>
    <a class="nav-link" style="left:198px">Wedding cakes</a>
    <a class="nav-link" style="left:640px">Price List</a>
    <a class="nav-link" style="left:732px">Our Cakes</a>
    <a class="nav-link" style="left:836px">Get in Touch</a>
  </nav>
  <div class="abs logo-card">
    <span class="logo-mark"></span>
    <span class="logo-name">Velvet Crumbhouse</span>
  </div>

  <section class="abs hero" role="img" aria-label="Slide photo of pink sugared and chocolate-striped cake pops in paper cases on a cooling rack">
    <div class="slider-arrow prev"><svg width="20" height="24" viewBox="0 0 20 24"><path d="M14 2 L5 12 L14 22" fill="none" stroke="#9a7f7c" stroke-width="2"/></svg></div>
    <div class="slider-arrow next"><svg width="20" height="24" viewBox="0 0 20 24"><path d="M6 2 L15 12 L6 22" fill="none" stroke="#9a7f7c" stroke-width="2"/></svg></div>
    <svg class="scroll-notch" viewBox="0 0 100 44"><path d="M0 44 C30 44 34 10 50 10 C66 10 70 44 100 44 Z" fill="#ffffff"/><path d="M41 24 L50 32 L59 24" fill="none" stroke="#555" stroke-width="2"/></svg>
  </section>

  <!-- Our story -->
  <div class="abs script-title" style="left:135px; top:690px">Discover</div>
  <h2 class="abs section-title" style="left:136px; top:778px">OUR STORY</h2>
  <div class="abs body-copy" style="left:138px; top:830px; width:455px">
    <p>Etiam est nunc venenatis in tristique eu imperdiet ac nisl Cum sociis natoque penatibus et magnis dis parturient montes nascetur ridiculus mus In iaculis facilisis massa Etiam eu urna Sed porta Suspendisse quam leo molestie</p>
    <p>Etiam est nunc venenatis in tristique eu imperdiet ac nisl Cum</p>
  </div>
  <div class="photo" style="left:618px; top:705px; width:225px; height:224px; background:linear-gradient(180deg,#dcdcd6 0%,#d98c8e 45%,#c77577 100%)" role="img" aria-label="Pink cake with white lace piping on a glass stand"></div>
  <div class="photo" style="left:856px; top:705px; width:226px; height:224px; background:linear-gradient(180deg,#e6d9c9 0%,#f0d9a3 50%,#c9c3b6 100%)" role="img" aria-label="Pale yellow cake topped with pink sugar flowers"></div>

  <!-- Banner one -->
  <section class="abs banner" style="top:969px; background:linear-gradient(100deg,#7a6a66 0%,#c7a7a8 35%,#8e8382 60%,#3f4a3c 100%)" role="img" aria-label="Photo of a white cake decorated with pink lilies">
    <div class="script-title">homemade</div>
    <div class="banner-caption">BEST CAKES</div>
  </section>

  <!-- Our cakes -->
  <div class="photo" style="left:133px; top:1267px; width:192px; height:133px; border-radius:16px 4px 4px 4px; background:linear-gradient(135deg,#d6b38f 0%,#c25a8c 45%,#f2ece6 100%)" role="img" aria-label="White cake with bright pink flowers"></div>
  <div class="photo" style="left:336px; top:1267px; width:191px; height:133px; border-radius:4px 16px 4px 4px; background:linear-gradient(135deg,#5e5a55 0%,#e9e4dc 55%,#b4aca2 100%)" role="img" aria-label="Tiered white cake with cream roses"></div>
  <div class="photo" style="left:133px; top:1411px; width:192px; height:133px; border-radius:4px 4px 4px 16px; background:linear-gradient(135deg,#e9e6e2 0%,#3a3434 50%,#ece9e6 100%)" role="img" aria-label="White cake with black damask pattern and bow"></div>
  <div class="photo" style="left:336px; top:1411px; width:191px; height:133px; border-radius:4px 4px 16px 4px; background:linear-gradient(135deg,#4b2a22 0%,#a77b6c 50%,#3a2019 100%)" role="img" aria-label="Topsy-turvy polka dot cake on a brown background"></div>

  <div class="abs script-title" style="left:637px; top:1265px">Discover</div>
  <h2 class="abs section-title" style="left:639px; top:1355px">OUR CAKES</h2>
  <div class="abs body-copy" style="left:643px; top:1404px; width:445px">
    <p>Etiam est nunc venenatis in tristique eu imperdiet ac nisl Cum sociis natoque penatibus et magnis dis parturient montes nascetur ridiculus mus In iaculis facilisis massa Etiam eu urna Sed porta Suspendisse quam leo molestie</p>
    <p>Etiam est nunc venenatis in tristique eu imperdiet ac nisl Cum</p>
  </div>

  <!-- Banner two -->
  <section class="abs banner" style="top:1596px; background:linear-gradient(100deg,#4a3a33 0%,#8c7468 35%,#a09a92 60%,#b9c4a8 80%,#6e6660 100%)" role="img" aria-label="Photo of chocolate and pistachio frosted cupcakes">
    <div class="script-title">Tastful</div>
    <div class="banner-caption">CHECK OUR PRICES</div>
  </section>

  <!-- Price list -->
  <div class="abs script-title" style="left:143px; top:1868px">Discover</div>
  <h2 class="abs section-title" style="left:142px; top:1955px">PRICE LIST</h2>
  <div class="abs body-copy" style="left:146px; top:2004px; width:445px">
    <p>Etiam est nunc venenatis in tristique eu imperdiet ac nisl Cum sociis natoque penatibus et magnis dis parturient montes nascetur ridiculus mus</p>
  </div>

  <div class="price-item" style="left:145px; top:2067px"><div class="price-name">Fusce tellus Sed metus</div><div class="price-value">$19.00 - $25.00</div></div>
  <div class="price-item" style="left:298px; top:2067px"><div class="price-name">Morbi diam mauris</div><div class="price-value">$19.00 - $25.00</div></div>
  <div class="price-item" style="left:436px; top:2067px"><div class="price-name">Curabitur iaculis</div><div class="price-value">$19.00 - $25.00</div></div>
  <div class="abs price-divider"></div>
  <div class="price-item" style="left:145px; top:2140px"><div class="price-name">Feugiat felis</div><div class="price-value">$19.00 - $25.00</div></div>
  <div class="price-item" style="left:298px; top:2140px"><div class="price-name">Morbi eget</div><div class="price-value">$19.00 - $25.00</div></div>
  <div class="price-item" style="left:436px; top:2140px"><div class="price-name">Suspendisse quam</div><div class="price-value">$19.00 - $25.00</div></div>

  <div class="photo" style="left:631px; top:1905px; width:224px; height:284px; background:linear-gradient(180deg,#e3d7c8 0%,#b88a6e 35%,#a06a48 60%,#2e2a24 100%)" role="img" aria-label="Cupcake with swirled caramel frosting and chopped nuts"></div>
  <div class="photo" style="left:869px; top:1905px; width:225px; height:284px; background:linear-gradient(135deg,#3c3442 0%,#a6adb8 45%,#d8d4dc 70%,#c8a8c6 100%)" role="img" aria-label="Cupcakes topped with white lace fondant discs"></div>

  <!-- Contact -->
  <section class="abs contact">
    <div class="script-title">Discover</div>
    <h2 class="section-title">CONTACT US</h2>
    <div class="field" style="left:447px; top:58px; width:207px; height:29px">First Name</div>
    <div class="field" style="left:663px; top:58px; width:209px; height:29px">Last Name</div>
    <div class="field" style="left:447px; top:94px; width:207px; height:29px">Email address</div>
    <div class="field" style="left:663px; top:94px; width:209px; height:29px">Phone</div>
    <div class="field" style="left:447px; top:131px; width:425px; height:80px">Message</div>
    <div class="submit-button">SUBMIT</div>
  </section>

  <footer class="abs footer">
    <svg class="footer-hump" width="150" height="41" viewBox="0 0 150 41"><path d="M0 41 C40 41 45 2 75 2 C105 2 110 41 150 41 Z" fill="#2f2f2f"/></svg>
    <p class="footer-note">© 2014 Company Name &nbsp;All right reserved &nbsp;Term of Use</p>
    <span class="social-dot" style="left:814px" aria-label="Social link"></span>
    <span class="social-dot" style="left:848px" aria-label="Social link"></span>
    <span class="social-dot" style="left:882px" aria-label="Social link"></span>
  </footer>

</body>
</html>
```